Thai Restaurant Billboard Design

Design a billboard promoting food delivery during this Coronavirus time. We want to grab attention by embracing the Coronavirus and offering food delivery. People are sitting at home and this is the right time to promote food delivery.

I have the logo and spec sheet attached.

Target Market(s)

Anyone.

Requirements
Must have
• Top Heading should be big and bold:

Coronavirus Got You Quarantined?

Then put under

We Deliver
Healthy Thai Food!
Put the logo that is attached
415-283-6071
Nice to have
• Eyecatching. Creative.
Should not have
• Don't have any not haves. Make it look good.

```html
<!DOCTYPE html>
<html lang="en">
<head>
<meta charset="utf-8">
<title>Baan Saeng Thai Kitchen – Delivery Billboard</title>
<link rel="stylesheet" href="https://fonts.googleapis.com/css2?family=Arimo:wght@400;700&display=swap">
<style>
  :root {
    --page-bg: #f3f3f3;
    --yellow-deep: #e9b62c;
    --yellow-light: #f7dc55;
    --red: #d3141b;
    --red-dark: #a50d12;
    --ink: #1e1a12;
    --white: #ffffff;
    --marble: #ecebe8;
  }
  * { box-sizing: border-box; margin: 0; padding: 0; }
  html, body {
    width: 1200px; height: 1000px; overflow: hidden;
    background: var(--page-bg);
    font-family: "Arimo", Arial, sans-serif;
  }
  .billboard {
    position: absolute; left: 58px; top: 322px;
    width: 1070px; height: 355px; overflow: hidden;
    background: linear-gradient(100deg, var(--yellow-deep) 0%, #f0c93c 45%, var(--yellow-light) 100%);
  }
  .food-gallery { position: absolute; inset: 0; }
  .headline-ribbon {
    position: absolute; left: 0; top: 34px;
    width: 500px; height: 46px;
    background: linear-gradient(180deg, var(--red) 0%, var(--red-dark) 100%);
    clip-path: polygon(0 0, 100% 0, 96% 100%, 0 100%);
    color: var(--white); font-weight: 700; font-size: 24px;
    line-height: 46px; padding-left: 24px; white-space: nowrap;
  }
  .lead-in {
    position: absolute; left: 23px; top: 92px;
    font-size: 30px; font-weight: 700; color: var(--ink);
  }
  .offer {
    position: absolute; left: 22px; top: 138px;
    font-size: 33px; font-weight: 700; line-height: 34px;
    color: var(--ink); text-transform: uppercase;
  }
  .phone-ribbon {
    position: absolute; left: 25px; top: 210px;
    width: 290px; height: 44px;
    display: flex; align-items: center; gap: 6px;
    padding-left: 30px;
    background: linear-gradient(180deg, var(--red) 0%, var(--red-dark) 100%);
    clip-path: polygon(5% 0, 100% 0, 95% 100%, 0 100%);
    color: var(--white); font-size: 28px; font-weight: 700;
  }
  .phone-ribbon::before {
    content: ""; position: absolute; left: 13px; top: 0;
    width: 6px; height: 100%;
    background: var(--yellow-light); transform: skewX(-30deg);
  }
  .phone-icon { width: 20px; height: 20px; fill: var(--white); }
  .brand {
    position: absolute; left: 24px; top: 276px;
    display: flex; align-items: center; gap: 12px;
  }
  .brand-square { width: 40px; height: 40px; background: var(--ink); }
  .brand-name {
    font-size: 26px; font-weight: 700; color: var(--ink); line-height: 1;
  }
</style>
</head>
<body>
  <section class="billboard">
    <svg class="food-gallery" width="1070" height="355" viewBox="0 0 1070 355">
      <defs>
        <radialGradient id="dish-noodles" cx="0.55" cy="0.5" r="0.6">
          <stop offset="0" stop-color="#e2cf9c"/><stop offset="1" stop-color="var(--marble)"/>
        </radialGradient>
        <radialGradient id="dish-rolls" cx="0.5" cy="0.5" r="0.6">
          <stop offset="0" stop-color="#ddd4c0"/><stop offset="1" stop-color="var(--marble)"/>
        </radialGradient>
        <radialGradient id="dish-larb" cx="0.6" cy="0.5" r="0.6">
          <stop offset="0" stop-color="#6e5a3c"/><stop offset="1" stop-color="var(--marble)"/>
        </radialGradient>
        <radialGradient id="dish-veg" cx="0.45" cy="0.5" r="0.6">
          <stop offset="0" stop-color="#7f9b55"/><stop offset="1" stop-color="var(--marble)"/>
        </radialGradient>
        <radialGradient id="dish-satay" cx="0.5" cy="0.55" r="0.6">
          <stop offset="0" stop-color="#e0c05a"/><stop offset="1" stop-color="var(--marble)"/>
        </radialGradient>
        <radialGradient id="dish-curry" cx="0.5" cy="0.5" r="0.6">
          <stop offset="0" stop-color="#e3a846"/><stop offset="1" stop-color="var(--marble)"/>
        </radialGradient>
      </defs>
      <polygon points="490,178 628,0 1070,0 1070,355 628,355" fill="var(--white)"/>
      <polygon role="img" aria-label="Photo of pad thai noodles with tofu and vegetables" points="494,176 630,0 800,0 677,176" fill="url(#dish-noodles)"/>
      <polygon role="img" aria-label="Photo of fresh rolls topped with jalapeño slices" points="677,176 800,0 987,0 852,176" fill="url(#dish-rolls)"/>
      <polygon role="img" aria-label="Photo of minced meat stir-fry with basil" points="852,176 987,0 1070,0 1070,176" fill="url(#dish-larb)"/>
      <polygon role="img" aria-label="Photo of stir-fried mixed vegetables" points="494,180 680,180 810,355 630,355" fill="url(#dish-veg)"/>
      <polygon role="img" aria-label="Photo of chicken satay skewers with peanut sauce" points="680,180 854,180 987,355 810,355" fill="url(#dish-satay)"/>
      <polygon role="img" aria-label="Photo of curry noodle soup in a bowl" points="854,180 1070,180 1070,355 987,355" fill="url(#dish-curry)"/>
      <g stroke="var(--yellow-light)" stroke-width="4" fill="none">
        <line x1="490" y1="178" x2="1070" y2="178"/>
        <line x1="800" y1="0" x2="677" y2="178"/>
        <line x1="987" y1="0" x2="852" y2="178"/>
        <line x1="680" y1="178" x2="810" y2="355"/>
        <line x1="854" y1="178" x2="987" y2="355"/>
      </g>
    </svg>

    <h1 class="headline-ribbon">Coronavirus Got You Quarantined?</h1>
    <p class="lead-in">Then put under</p>
    <h2 class="offer">We Deliver<br>Healthy Thai Food!</h2>
    <div class="phone-ribbon">
      <svg class="phone-icon" viewBox="0 0 24 24" aria-hidden="true"><path d="M6.6 10.8a15.1 15.1 0 0 0 6.6 6.6l2.2-2.2a1 1 0 0 1 1-.25 11.4 11.4 0 0 0 3.6.57 1 1 0 0 1 1 1V20a1 1 0 0 1-1 1A17 17 0 0 1 3 4a1 1 0 0 1 1-1h3.5a1 1 0 0 1 1 1c0 1.25.2 2.45.57 3.57a1 1 0 0 1-.25 1z"/></svg>
      <span>415-283-6071</span>
    </div>
    <div class="brand">
      <span class="brand-square" aria-hidden="true"></span>
      <span class="brand-name">Baan Saeng Thai Kitchen</span>
    </div>
  </section>
</body>
</html>
```